Design a business card & stationary for a mortgage company

We are looking for a good looking business card design for our mortgage company that includes our logo. We received a free design as part of our logo project but we don't love it. The company is called "Pinecrest Mortgage Company" so we like waves and lighthouses. The logo should be included. We have a version in both vertical and horizontal that we have provided.

Industry/Entity Type

Finance

Contact Information for Business Card

This should include our new logo file

Requirements
Must have
• 3. The details you'd like on the card - name, title, phone, email, website, address, social media handles etc.
1. Marcus Hale
Vice President
302-419-6253
Fax 888-304-2918
mhale@pinecrestmortgage.example
NMLS 47162 - Company NMLS 61290
18 Larkin Ave
Brightwater, DE 08614

```html
<!DOCTYPE html>
<html lang="en">
<head>
<meta charset="utf-8">
<title>Pinecrest Mortgage Company – Business Card</title>
<link rel="stylesheet" href="https://fonts.googleapis.com/css2?family=Montserrat:wght@400;500;800&display=swap">
<style>
  :root{
    --page:#e2e2e2;
    --navy-top:#0c4a8f;
    --navy-bottom:#05275a;
    --ink:#0d3a75;
    --accent:#1b82dc;
    --text:#2a2a2a;
    --white:#ffffff;
  }
  *{box-sizing:border-box;margin:0;padding:0}
  html,body{width:686px;height:1200px;overflow:hidden;background:var(--page)}
  body{font-family:"Montserrat",sans-serif;position:relative}
  .card{
    position:absolute;left:99px;width:490px;height:280px;overflow:hidden;
    box-shadow:0 2px 6px rgba(0,0,0,.18);
  }
  .card--front{top:540px;background:linear-gradient(180deg,var(--navy-top),var(--navy-bottom))}
  .card--back{top:870px;background:var(--white)}

  .front-decoration{
    position:absolute;left:0;top:20px;width:130px;height:240px;
    background:radial-gradient(ellipse at 30% 40%,rgba(40,120,220,.45),rgba(20,80,170,.12) 60%,rgba(0,0,0,0) 75%);
  }
  .front-wordmark{
    position:absolute;left:156px;top:100px;display:flex;align-items:center;gap:10px;
  }
  .front-wordmark .mark-dot{width:14px;height:14px;border-radius:50%;background:var(--white);flex:none}
  .front-wordmark .name{
    color:var(--white);font-weight:500;font-size:21px;line-height:1.2;
    letter-spacing:.1em;text-transform:uppercase;
  }

  .back-decoration{
    position:absolute;left:270px;top:0;width:220px;height:280px;
    background:radial-gradient(ellipse at 80% 60%,rgba(11,60,130,.85),rgba(20,80,160,.35) 45%,rgba(255,255,255,0) 75%);
  }
  .back-wordmark{
    position:absolute;left:38px;top:30px;display:flex;align-items:center;gap:7px;
  }
  .back-wordmark .mark-dot{width:9px;height:9px;border-radius:50%;background:var(--ink);flex:none}
  .back-wordmark .name{
    color:var(--ink);font-weight:500;font-size:12px;line-height:1.25;
    letter-spacing:.07em;text-transform:uppercase;
  }
  .person{position:absolute;left:37px;top:94px}
  .person .full-name{color:var(--ink);font-weight:800;font-size:19px;letter-spacing:.03em;text-transform:uppercase;line-height:1.1}
  .person .title{color:var(--text);font-size:9.5px;letter-spacing:.02em;text-transform:uppercase;margin-top:3px}
  .contacts{position:absolute;left:35px;top:152px;list-style:none}
  .contacts li{display:flex;align-items:center;gap:10px;height:23px;color:var(--text);font-size:9.5px;line-height:1.2}
  .contacts .icon{width:18px;height:18px;flex:none}
  .contacts li.address{height:28px}
</style>
</head>
<body>

<section class="card card--front" aria-label="Card front" style="top:96px">
  <div class="front-decoration" role="img" aria-label="Faint coastal emblem decoration"></div>
  <div class="front-wordmark">
    <span class="mark-dot"></span>
    <div class="name">Pinecrest<br>Mortgage Company</div>
  </div>
</section>

<section class="card card--back" aria-label="Card back" style="top:426px">
  <div class="back-decoration" role="img" aria-label="Large coastal emblem decoration"></div>
  <div class="back-wordmark">
    <span class="mark-dot"></span>
    <div class="name">Pinecrest<br>Mortgage Company</div>
  </div>

  <div class="person">
    <div class="full-name">Marcus Hale</div>
    <div class="title">Vice President</div>
  </div>

  <ul class="contacts">
    <li>
      <svg class="icon" viewBox="0 0 22 22"><circle cx="11" cy="11" r="10" fill="none" stroke="#1b82dc" stroke-width="1.3"/><path d="M7.5 6.5l2 0 .8 2.4-1.2 1a6 6 0 0 0 3 3l1-1.2 2.4.8v2a1 1 0 0 1-1 1A8 8 0 0 1 6.5 7.5a1 1 0 0 1 1-1z" fill="none" stroke="#0d3a75" stroke-width="1.1"/></svg>
      <span>302-419-6253</span>
    </li>
    <li>
      <svg class="icon" viewBox="0 0 22 22"><circle cx="11" cy="11" r="10" fill="none" stroke="#1b82dc" stroke-width="1.3"/><rect x="7" y="8" width="3" height="7" fill="#0d3a75"/><rect x="10.5" y="6.5" width="5" height="8.5" fill="none" stroke="#0d3a75" stroke-width="1"/><path d="M11.5 9h3M11.5 11h3M11.5 13h3" stroke="#0d3a75" stroke-width=".8"/></svg>
      <span>888-304-2918</span>
    </li>
    <li>
      <svg class="icon" viewBox="0 0 22 22"><circle cx="11" cy="11" r="10" fill="none" stroke="#1b82dc" stroke-width="1.3"/><rect x="6.5" y="7.5" width="9" height="7" fill="#0d3a75"/><path d="M6.5 7.5l4.5 4 4.5-4" fill="none" stroke="#fff" stroke-width=".9"/></svg>
      <span>mhale@pinecrestmortgage.example</span>
    </li>
    <li class="address">
      <svg class="icon" viewBox="0 0 22 22"><circle cx="11" cy="11" r="10" fill="none" stroke="#1b82dc" stroke-width="1.3"/><circle cx="11" cy="11" r="5" fill="#0d3a75"/><path d="M6 11h10M11 6v10M8 7.5q3 3.5 0 7M14 7.5q-3 3.5 0 7" fill="none" stroke="#fff" stroke-width=".7"/></svg>
      <span>NMLS 47162 - Company NMLS 61290<br>18 Larkin Ave Brightwater, DE 08614</span>
    </li>
  </ul>
</section>

</body>
</html>
```